QRT Tea House - design for coffee company logo and 12 oz coffee bags

I would like to start selling coffee and need both a brand logo as well as packaging design for the coffee bags. The name of the company is QRT Tea House. I have a related brand for a youtube channel called QRTBLD4K, I will attach that logo to the uploaded files. The branding for the coffee should compliment QRTBLD4K, but doesn't have to (and probably should NOT be too close in similarity). The Company Brand logo should be featured on the bag, but not as dominant/large as the specific product label (like Glider 3400).
This coffee will be marketed towards aviation consumers. Pilots, dispatchers, ATC professionals, mechanics, etc. Male dominated market. Masculine themes needed.
For the bag design, I need one standard bag design to use across all my products, then I will simply add the SKU product names to all the interchangeable bags. So my design request is for a dark bag with airspace lines/designs/graphics in a repeatable format that I can cast to the printing design. I am adding inspiration upload for this. I'm thinking using a light or white color for the shapes/vectors/symbols on the dark bag. Not all of the different shapes and icons should be included, but things like the compass circle with tick marks, line vectors stretching out in different directions. Again - don't need ALL of the shapes and text. certainly not the green stuff. And important to note, the inspiration uploads I've provided have white background and darker lines/shapes. I would like to inverse that for this design. Dark bag and light shapes/lines.
If you could include the first product label for the bag, that would be great. The first coffee product will be called "Glider 3400". I've included an example I tried to make on Figma, but I'm an awful designer. The example I included has the "1200" on an aviation transponder. This is the code plugged into the airplane that lets ATC know who you are and where you are. In the final delivery, I would like the product label (Glider 3400) to be separate from the bag itself so I can change it out with other coffee product labels for my light and dark roasts. A section at the bottom with roast profile, grind type, source, etc should be located on the bottom (or wherever it makes sense). The inspiration for the layout could come from the lower section of the Approach Plate i attached.
On the back, a section that notes details about the company:
"QRT Tea House was built for people who start the day with somewhere to go — pilots, builders, travelers, early risers, and anyone chasing the next leg of the journey.
QRT is a nod to our home skies under Hollis Ridge Center and to Zero Fuel Weight — the aviation reminder that every mission starts with what you choose to carry.
Fuel Your Mission."

Where the package opens at the top, a horizontal image that says "REMOVE BEFORE FLIGHT" is a nice to have. Inspiration image uploaded to the brief. This is a standard cover on aircraft to protect sensitive instruments/equipment. Located right where the folded seal of the bag is would be a nice touch. Red with white text.

Target Market(s)

aviation professionals and enthusiasts... who like coffee. Pilots, dispatchers, military, Air Traffic Control, Mechanics. Mostly male crowd.

Industry/Entity Type

Coffee company, but aviation style branding

Requirements
Nice to have
• company tagline "Fuel Your Mission" - experiment with placing - either under company logo - on sides/back - whatever looks/feels right.
Should not have
• do not include the uploaded QRT BLD4K logo on the package. It's for reference as a sister brand only.

```html
<!DOCTYPE html>
<html lang="en">
<head>
<meta charset="utf-8">
<title>QRT Tea House – Glider 3400 bag front</title>
<link rel="stylesheet" href="https://fonts.googleapis.com/css2?family=Anton&family=Orbitron:wght@500&family=Roboto+Condensed:wght@400;500;700&display=swap">
<style>
  :root {
    --page: #f1f1f1;
    --bag: #070707;
    --bag-top: #161616;
    --chart-line: #3a3a3a;
    --flag-red: #ee1c13;
    --white: #ffffff;
    --label-black: #050505;
    --label-edge: #5a5a5a;
    --frame-orange: #e2662a;
    --digit-orange: #f35a1d;
    --peach: #fdd6a6;
    --ink: #111111;
  }
  * { margin: 0; padding: 0; box-sizing: border-box; }
  html, body { width: 1200px; height: 768px; overflow: hidden; background: var(--page); }
  body { position: relative; font-family: "Roboto Condensed", Arial, sans-serif; }

  .bag-front {
    position: absolute; left: 395px; top: 14px;
    width: 409px; height: 739px;
    background: var(--bag); overflow: hidden;
  }
  .chart-pattern {
    position: absolute; left: 0; top: 38px; width: 100%; height: 701px;
    background: radial-gradient(ellipse at 50% 30%, #141414 0%, var(--bag) 70%);
  }
  .seal-strip { position: absolute; left: 0; top: 0; width: 100%; height: 38px; background: var(--bag-top); }
  .flight-tag {
    position: absolute; left: 74px; top: 0; width: 261px; height: 38px;
    background: var(--flag-red); color: var(--white);
    font-size: 16px; font-weight: 500; letter-spacing: 0.2px;
    display: flex; align-items: center; justify-content: center;
  }
  .brand-name {
    position: absolute; left: 0; top: 214px; width: 100%;
    text-align: center; font-family: "Anton", Impact, sans-serif;
    font-size: 50px; line-height: 60px; color: var(--white); letter-spacing: 1px;
  }

  .product-label {
    position: absolute; left: 22px; top: 288px; width: 365px; height: 425px;
    background: var(--label-black); border: 1.5px solid var(--label-edge); border-radius: 29px;
  }
  .label-frame {
    position: absolute; left: 9px; top: 11px; width: 346px; height: 399px;
    border: 2px solid var(--frame-orange); border-radius: 24px; overflow: hidden;
  }
  .product-name { position: absolute; left: 23px; top: 25px; width: 300px; height: 80px; }
  .product-name text { font-family: "Anton", Impact, sans-serif; fill: var(--white); }

  .transponder {
    position: absolute; left: 33px; top: 99px; width: 284px; height: 59px;
    border-radius: 14px; border: 2px solid #3c3c3c;
    background: linear-gradient(90deg, #1b1b1b 0%, #2a2a2a 55%, #8a8a8a 100%);
  }
  .transponder-knob {
    position: absolute; left: 16px; top: 12px; width: 33px; height: 33px; border-radius: 50%;
    background: radial-gradient(circle at 35% 35%, #3a3a3a, #0c0c0c 70%);
  }
  .transponder-display {
    position: absolute; left: 63px; top: 4px; width: 173px; height: 47px;
    border-radius: 10px; border: 1.5px solid #cfcfcf;
    background: linear-gradient(180deg, #050505, #1a1a1a);
    color: var(--digit-orange); font-family: "Orbitron", monospace;
    font-size: 34px; letter-spacing: 4px;
    display: flex; align-items: center; justify-content: center;
  }

  .tagline {
    position: absolute; left: 0; top: 176px; width: 100%; text-align: center;
    color: var(--peach); font-size: 15px; font-weight: 700; letter-spacing: 3px;
  }
  .tagline-rule { position: absolute; top: 192px; height: 1px; background: var(--frame-orange); width: 31px; }
  .tagline-rule.left { left: 34px; }
  .tagline-rule.right { right: 25px; }
  .plane-mark {
    position: absolute; left: 121px; top: 200px; width: 117px; height: 30px;
    background: radial-gradient(ellipse at 50% 60%, var(--peach) 0%, rgba(253,214,166,0.5) 35%, transparent 70%);
  }

  .spec-panel {
    position: absolute; left: 0; top: 242px; width: 100%; height: 115px;
    background: var(--peach); color: var(--ink);
  }
  .spec-col { position: absolute; top: 10px; text-align: center; }
  .spec-col h3 { font-size: 11px; font-weight: 700; line-height: 13px; }
  .spec-col p { font-size: 9px; font-weight: 500; line-height: 11px; margin-top: 6px; }
  .spec-col.roast { left: 0; width: 131px; }
  .spec-col.grind { left: 131px; width: 115px; }
  .spec-col.origin { left: 246px; width: 106px; }
  .spec-divider { position: absolute; top: 2px; width: 1px; height: 73px; background: var(--ink); }
  .spec-rule { position: absolute; left: 14px; top: 75px; width: 322px; height: 1px; background: var(--ink); }
  .roast-dots { display: flex; gap: 3px; justify-content: center; margin-top: 6px; }
  .roast-dots span { width: 9px; height: 9px; border-radius: 50%; border: 1px solid var(--ink); }
  .roast-dots span.on { background: var(--ink); }
  .bean-icon { display: block; margin: 5px auto 0; }
  .tasting-title { position: absolute; top: 80px; width: 100%; text-align: center; font-size: 9px; letter-spacing: 2px; font-weight: 500; }
  .tasting-notes { position: absolute; top: 94px; width: 100%; text-align: center; font-size: 11px; letter-spacing: 2.4px; font-weight: 700; }

  .net-weight {
    position: absolute; top: 373px; width: 100%; text-align: center;
    color: var(--peach); font-size: 11px; font-weight: 700; letter-spacing: 3px;
  }
</style>
</head>
<body>
  <main class="bag-front">
    <div class="chart-pattern" role="img" aria-label="Light airspace chart lines, compass roses and route labels on black"></div>
    <div class="seal-strip"></div>
    <div class="flight-tag">REMOVE BEFORE YOU FLY</div>

    <div class="brand-name">QRT</div>

    <section class="product-label">
      <div class="label-frame">
        <svg class="product-name" viewBox="0 0 300 80" aria-label="Glider">
          <text x="2" y="72" font-size="82" textLength="296" lengthAdjust="spacingAndGlyphs">GLIDER</text>
        </svg>

        <div class="transponder">
          <div class="transponder-knob"></div>
          <div class="transponder-display">3400</div>
        </div>

        <div class="tagline-rule left"></div>
        <p class="tagline">Unleash your momentum</p>
        <div class="tagline-rule right"></div>
        <div class="plane-mark" role="img" aria-label="Small aircraft silhouette"></div>

        <div class="spec-panel">
          <div class="spec-col roast">
            <h3>ROAST PROFILE</h3>
            <p>MEDIUM-DARK</p>
            <div class="roast-dots"><span class="on"></span><span class="on"></span><span class="on"></span><span></span><span></span></div>
          </div>
          <div class="spec-divider" style="left:131px"></div>
          <div class="spec-col grind">
            <h3>GRIND TYPE</h3>
            <p>WHOLE BEAN</p>
            <svg class="bean-icon" width="14" height="16" viewBox="0 0 14 16" aria-hidden="true">
              <ellipse cx="7" cy="8" rx="5.5" ry="7.5" transform="rotate(25 7 8)" fill="#111"/>
              <path d="M9 2 C5 6 9 10 5 14" stroke="#fdd6a6" stroke-width="1.2" fill="none"/>
            </svg>
          </div>
          <div class="spec-divider" style="left:246px"></div>
          <div class="spec-col origin">
            <h3>ORIGIN</h3>
            <p>BRAZIL+<br>COLUMBIA</p>
          </div>
          <div class="spec-rule"></div>
          <p class="tasting-title">TASTING NOTES</p>
          <p class="tasting-notes">DARK CHOCOLATE . TOASTED NUT . CARAMEL</p>
        </div>

        <p class="net-weight">NET WT. 12 OZ &nbsp;(340 OG)</p>
      </div>
    </section>
  </main>
</body>
</html>
```